Lumora aesthetics offers a range of facial aesthetics treatments by a fully qualified dentist, to a high end crowd. Treatments include antiwrinkle treatment, the use of dermal fillers to provide facial volumisation and rejuvenation and also lip volumisation.
I want a luxurious and bold look. Black background with a bold striking gold logo in the centre possibly incorporating the outline of a face in a subtle yet effective way. I want it to include the work I offer so people will be aware of what they are looking into but not look like there's too much on the card, So it's a clean look.
At the bottom I would like it to say by Dr. Meera Sandhu. Alongside my email address and mobile number.

```html
<!DOCTYPE html>
<html lang="en">
<head>
<meta charset="utf-8">
<title>Lumora aesthetics – Business Card</title>
<link href="https://fonts.googleapis.com/css2?family=Open+Sans:wght@400;600&display=swap" rel="stylesheet">
<style>
  :root {
    --page: #d9d9d9;
    --card-dark: #252525;
    --band-grey: #4b4b4b;
    --gold: #d4ae32;
    --gold-deep: #a8891f;
    --ink: #2a2a2a;
    --paper: #ffffff;
    --soft: #e6e6e6;
  }
  * { margin: 0; padding: 0; box-sizing: border-box; }
  html, body { width: 1200px; height: 1200px; overflow: hidden; }
  body {
    background: var(--page);
    font-family: "Open Sans", Arial, sans-serif;
    position: relative;
  }
  .card {
    position: absolute;
    left: 100px; top: 310px;
    width: 1000px; height: 580px;
    background: var(--card-dark);
    box-shadow: 0 14px 40px rgba(0,0,0,.25);
    overflow: hidden;
  }
  .brand-panel {
    position: absolute; left: 0; top: 0;
    width: 560px; height: 100%;
  }
  .brand-mark {
    position: absolute; left: 165px; top: 36px;
    width: 230px; height: 230px;
    border: 6px solid var(--gold);
    border-radius: 50%;
    display: flex; align-items: center; justify-content: center;
  }
  .brand-name {
    color: var(--gold);
    font-weight: 600;
    font-size: 26px;
    text-align: center;
    line-height: 1.25;
  }
  .doctor-name {
    position: absolute; left: 0; width: 560px; top: 296px;
    text-align: center;
    color: var(--gold);
    font-size: 40px;
    font-weight: 400;
    line-height: 56px;
  }
  .tagline-band {
    position: absolute; left: 0; top: 370px;
    width: 590px; height: 58px;
    background: var(--band-grey);
    display: flex; align-items: center;
  }
  .tagline {
    width: 560px;
    text-align: center;
    color: var(--soft);
    font-size: 22px;
    line-height: 1;
  }
  .treatments {
    position: absolute; left: 0; width: 560px; top: 462px;
    list-style: none;
    display: flex; justify-content: center; gap: 14px;
    color: var(--gold);
    font-size: 17px;
    letter-spacing: .3px;
  }
  .treatments li + li::before {
    content: "•";
    margin-right: 14px;
    color: var(--soft);
  }
  .divider-strip {
    position: absolute; left: 560px; top: 0;
    width: 30px; height: 100%;
    background: var(--band-grey);
  }
  .contact-panel {
    position: absolute; left: 590px; top: 0;
    width: 410px; height: 100%;
    background: var(--gold);
    padding: 70px 40px 0 30px;
  }
  .contact-row {
    display: flex; gap: 22px; align-items: flex-start;
    padding: 18px 0;
    border-bottom: 2px solid var(--gold-deep);
  }
  .contact-row:last-child { border-bottom: none; }
  .contact-icon { width: 30px; height: 30px; flex: none; margin-top: 2px; }
  .contact-text {
    color: var(--paper);
    font-size: 23px;
    line-height: 1.3;
  }
</style>
</head>
<body>
  <div class="card">
    <div class="brand-panel">
      <div class="brand-mark">
        <span class="brand-name">Lumora<br>aesthetics</span>
      </div>
      <p class="doctor-name">Dr. Meera Sandhu</p>
      <div class="tagline-band">
        <p class="tagline">Committed to excellence.</p>
      </div>
      <ul class="treatments">
        <li>Anti-wrinkle</li>
        <li>Dermal fillers</li>
        <li>Lip volumisation</li>
      </ul>
    </div>
    <div class="divider-strip"></div>
    <div class="contact-panel">
      <div class="contact-row">
        <svg class="contact-icon" viewBox="0 0 24 24" aria-hidden="true">
          <path fill="#2a2a2a" d="M6.6 2.5l2.6 3.8-1.8 2c.9 2.6 2.8 5 5.8 6.8l2-1.7 3.9 2.5-1.4 3.3c-.4.8-1.3 1.2-2.2 1-7-1.8-11.700-7.600-12.6-13.6-.1-.9.4-1.7 1.2-2l2.5-2.1z"/>
        </svg>
        <p class="contact-text">+000 . 5550 . 1120<br>+000 . 5550 . 1121</p>
      </div>
      <div class="contact-row">
        <svg class="contact-icon" viewBox="0 0 24 24" aria-hidden="true">
          <g fill="none" stroke="#2a2a2a" stroke-width="1.8">
            <circle cx="12" cy="12" r="10"/>
            <ellipse cx="12" cy="12" rx="4.5" ry="10"/>
            <line x1="2" y1="12" x2="22" y2="12"/>
            <path d="M4 6.5h16M4 17.5h16"/>
          </g>
        </svg>
        <p class="contact-text">meera@lumoramail.com<br>lumoraclinic.com</p>
      </div>
      <div class="contact-row">
        <svg class="contact-icon" viewBox="0 0 24 24" aria-hidden="true">
          <path fill="#2a2a2a" d="M12 1.5a7.5 7.5 0 0 0-7.5 7.5c0 5.6 7.5 13.5 7.5 13.5S19.5 14.6 19.5 9A7.5 7.5 0 0 0 12 1.5zm0 10.5a3 3 0 1 1 0-6 3 3 0 0 1 0 6z"/>
        </svg>
        <p class="contact-text">214 Larch Street<br>Fairhaven NY 54321</p>
      </div>
    </div>
  </div>
</body>
</html>
```